Lotven Pharma Chinese Traditional Medicine Web Design

We need a web design for a new company based in Shanghai China called 'Lotven Pharma'. We develop Chinese traditional herbal medicine, including research and development, technical support service, manufacturing, . Also, there’s a small ratio of western medicine. Our goal is to contributing to a healthier future.

Target Market(s)

global,but mainly China

Industry/Entity Type

Pharmaceutical

Number of Pages Required

1 page

Font styles to use
Serif

Colors
e4daeb
cedeed
cadf82
eaf2ce
fbd4d5
fee3d4
fabb94
fee18a
b8a6cd

Requirements
Must have
• triditional Chinese elements, concept of herbal, health, value, better life for people..could be colourful but not more than 3 different colour..
Nice to have
• Style: simple, communicate traditional Chinese herbal medicine element, as well as modern technique..same as LOGO style..
Should not have
• please dont show more IT elements...

```html
<!DOCTYPE html>
<html lang="en">
<head>
<meta charset="utf-8">
<title>Lotven Pharma – Company Overall</title>
<link rel="stylesheet" href="https://fonts.googleapis.com/css2?family=Tinos&family=Open+Sans:wght@400&display=swap">
<style>
:root{
  --brown:#67371f;
  --brown-title:#6b3520;
  --green:#404a40;
  --green-circle:#4a5a4a;
  --ink:#2f2f2f;
  --nav:#4a4a4a;
  --white:#ffffff;
  --footer-bg:#f3f2f0;
  --rule:#c9a98f;
}
*{margin:0;padding:0;box-sizing:border-box}
html,body{width:1200px;height:2850px;overflow:hidden;background:var(--white)}
body{position:relative;font-family:"Open Sans",sans-serif;color:var(--ink)}
.serif{font-family:"Tinos",serif}
section,header,footer{position:absolute;left:0;width:1200px}

/* header */
.site-header{top:0;height:95px;background:var(--white)}
.brand{position:absolute;left:124px;top:28px;display:flex;align-items:center;gap:8px}
.brand-dot{width:30px;height:30px;border-radius:50%;background:var(--brown)}
.brand-name{font-family:"Tinos",serif;font-size:14px;color:var(--brown);line-height:1.1}
.main-nav{position:absolute;right:60px;top:36px;display:flex;gap:28px;font-family:"Tinos",serif;font-size:17px;color:var(--nav)}
.main-nav .active{color:#222}

/* hero */
.hero{top:95px;height:423px}
.hero-photo{position:absolute;inset:0;background:linear-gradient(100deg,#7a6448 0%,#a88a5e 30%,#c9a874 55%,#8d6a47 75%,#b08a58 100%)}
.hero-badge{position:absolute;left:126px;top:87px;width:276px;height:276px;border-radius:50%;background:#7f8a7c;display:flex;align-items:center;justify-content:center}
.hero-badge-inner{width:256px;height:256px;border-radius:50%;background:var(--green-circle);display:flex;align-items:center;justify-content:center;text-align:center}
.hero-badge h1{font-family:"Tinos",serif;font-weight:400;color:var(--white);font-size:33px;line-height:37px}

/* intro */
.intro{top:518px;height:570px;text-align:center}
.section-title{font-family:"Tinos",serif;font-weight:400;color:var(--brown-title);font-size:36px}
.intro .section-title{position:absolute;top:128px;width:100%}
.intro-text{position:absolute;top:198px;left:150px;width:906px;font-size:14.5px;line-height:23.5px;color:var(--ink)}
.intro-text p{margin-bottom:23.5px}

/* abilities */
.abilities{top:1088px;height:492px;background:var(--brown);color:var(--white)}
.abilities h2{position:absolute;left:113px;top:100px;font-family:"Tinos",serif;font-weight:400;font-size:36px}
.ability-list{position:absolute;top:178px;left:116px;width:1000px;list-style:none;display:grid;grid-template-columns:523px 477px;row-gap:23px}
.ability-list li{position:relative;padding-left:25px;font-size:15.5px;line-height:23.5px}
.ability-list li::before{content:"";position:absolute;left:2px;top:8px;width:9px;height:9px;border-radius:50%;background:var(--white)}

/* partners */
.partners{top:1580px;height:465px}
.partners .section-title{position:absolute;top:92px;width:100%;text-align:center;left:-6px}
.partner-badge{position:absolute;width:100px;height:30px;background:#8c8c8c;border-radius:4px}
.partner-badge.round{width:70px;height:70px;border-radius:50%}

/* culture */
.culture{top:2045px;height:451px;background:var(--green);color:var(--white)}
.culture-photo{position:absolute;left:156px;top:55px;width:338px;height:338px;border-radius:50%;background:radial-gradient(circle at 45% 40%,#e8e2d8 0%,#b48a62 35%,#7a4a2e 70%,#4e2d1c 100%)}
.culture h2{position:absolute;left:542px;top:96px;font-family:"Tinos",serif;font-weight:400;font-size:36px}
.culture-text{position:absolute;left:544px;top:150px;width:520px;font-size:15.5px;line-height:23px}
.culture-text p{margin-bottom:23px}

/* footer */
.site-footer{top:2496px;height:354px;background:var(--footer-bg)}
.footer-brand{position:absolute;left:134px;top:60px;display:flex;align-items:center;gap:10px}
.footer-brand .brand-dot{width:40px;height:40px}
.footer-brand .brand-name{font-size:17px}
.reg{position:absolute;left:137px;top:155px;font-size:17px;line-height:31px;color:#333}
.footer-col{position:absolute;top:50px}
.footer-col h3{font-family:"Tinos",serif;font-weight:400;font-size:18px;color:#3a3a3a;margin-bottom:8px;letter-spacing:.3px}
.footer-col ul{list-style:none;padding-left:4px}
.footer-col li{font-size:15.5px;line-height:31px;color:#3a3a3a}
.col-links{left:435px}
.col-resources{left:643px}
.col-resources ul{padding-left:8px}
.col-address{left:817px}
.address{display:flex;gap:10px;margin-top:4px;font-size:15.5px;line-height:23px;color:#333}
.socials{display:flex;gap:5px;margin-top:24px;margin-left:-5px}
.socials span{width:39px;height:39px;border-radius:50%;border:2px solid var(--brown)}
.footer-rule{position:absolute;left:120px;top:288px;width:964px;height:1px;background:var(--rule)}
.copyright{position:absolute;top:308px;width:100%;text-align:center;left:-6px;font-size:14px;color:#333}
</style>
</head>
<body>

<header class="site-header">
  <div class="brand"><span class="brand-dot"></span><span class="brand-name">LOTVEN PHARMA</span></div>
  <nav class="main-nav">
    <span class="active">HOME</span><span>COMPANY OVERALL</span><span>NEWS</span><span>PRODUCTS</span><span>SERVICES</span><span>CAREER</span><span>CONTACT</span>
  </nav>
</header>

<section class="hero">
  <div class="hero-photo" role="img" aria-label="Dried Chinese herbs, root slices and bamboo mat on a wooden table"></div>
  <div class="hero-badge"><div class="hero-badge-inner"><h1>COMPANY<br>OVERALL</h1></div></div>
</section>

<section class="intro">
  <h2 class="section-title">COMPANY INTRODUCTION</h2>
  <div class="intro-text">
    <p>hendrerit quis leo Pellentesque rutrum malesuada neque Nunc tempus felis vitae urna Vivamus porttitor neque at volutpat rutrum purus nisi eleifend libero a tempus libero lectus feugiat felis Morbi diam mauris viverra in gravida eu mattis in ante Morbi eget arcu</p>
    <p>Morbi porta libero id ullamcorper nonummy nibh ligula pulvinar metus eget consectetuer augue nisi quis lacus Ut ac mi quis lacus mollis aliquam Curabitur iaculis tempus eros Curabitur vel mi sit amet magna malesuada ultrices Ut nisi erat fermentum vel congue id euismod in elit hendrerit quis leo Pellentesque rutrum malesuada neque Nunc tempus felis vitae urna Vivamus porttitor neque at volutpat rutrum purus nisi eleifend libero a tempus libero lectus feugiat felis Morbi diam mauris viverra in gravida eu mattis in ante Morbi eget arcu</p>
    <p>Morbi porta libero id ullamcorper nonummy nibh ligula pulvinar metus eget consectetuer augue nisi quis lacus Ut ac mi quis lacus mollis aliquam Curabitur iaculis tempus eros Curabitur vel mi sit amet magna malesuada</p>
  </div>
</section>

<section class="abilities">
  <h2>KEY ABILITIES</h2>
  <ul class="ability-list">
    <li>Curabitur vel mi sit amet magna malesuada ultrices Ut nisi erat fermentum vel congue id euismod in elit</li>
    <li>Pendrerit quis leo Pellentesque rutrum malesuada neque Nunc tempus felis vitae urna Vivamus</li>
    <li>Fusce ultricies orci ac feugiat suscipit leo massa sodales velit et scelerisque quam Curabitur vel dolor</li>
    <li>Aorttitor neque at volutpat rutrum purus nisi eleifend libero a tempus libero lectus feugiat felis Morbi diam</li>
    <li>Altrices ipsum dictum tristique Praesent vitae lacus Ut velit enim vestibulum non fermentum nec</li>
    <li>Mauris viverra in gravida eu mattis in anquam Curabitur vel dolor ultrices ipsum dictum tristique</li>
  </ul>
</section>

<section class="partners">
  <h2 class="section-title">PARTNERS</h2>
  <div class="partner-badge" style="left:142px;top:191px"></div>
  <div class="partner-badge" style="left:344px;top:191px"></div>
  <div class="partner-badge" style="left:521px;top:191px"></div>
  <div class="partner-badge" style="left:727px;top:191px"></div>
  <div class="partner-badge" style="left:920px;top:191px"></div>
  <div class="partner-badge round" style="left:158px;top:288px"></div>
  <div class="partner-badge" style="left:344px;top:307px"></div>
  <div class="partner-badge" style="left:531px;top:307px"></div>
  <div class="partner-badge" style="left:727px;top:307px"></div>
  <div class="partner-badge" style="left:928px;top:307px"></div>
</section>

<section class="culture">
  <div class="culture-photo" role="img" aria-label="White mortar and pestle surrounded by dried herbal roots and bark"></div>
  <h2>CULTURE</h2>
  <div class="culture-text">
    <p>hendrerit quis leo Pellentesque rutrum malesuada neque Nunc tempus felis vitae urna Vivamus porttitor neque at volutpat rutrum purus nisi eleifend libero a tempus libero lectus feugia</p>
    <p>Morbi porta libero id ullamcorper nonummy nibh ligula pulvinar metus eget consectetuer augue nisi quis lacus Ut ac mi quis lacus mollis aliquam Curabitur iaculis tempus eros Curabitur vel mi sit amet magna malesuada ultrices Ut nisi erat fermentum vel congue id</p>
  </div>
</section>

<footer class="site-footer">
  <div class="footer-brand"><span class="brand-dot"></span><span class="brand-name">LOTVEN PHARMA<br>洛文医药</span></div>
  <div class="reg">Registration no.<br>12010000000000</div>
  <div class="footer-col col-links">
    <h3>QUICK LINKS</h3>
    <ul><li>Home</li><li>Company overall</li><li>News</li><li>Products</li></ul>
  </div>
  <div class="footer-col col-resources">
    <h3>RESOURCES</h3>
    <ul><li>Services</li><li>Career</li><li>Contact</li></ul>
  </div>
  <div class="footer-col col-address">
    <h3>OUR ADDRESS</h3>
    <div class="address">
      <svg width="24" height="34" viewBox="0 0 24 34" aria-hidden="true"><path d="M12 0C5.4 0 0 5.2 0 11.7 0 20 12 34 12 34s12-14 12-22.3C24 5.2 18.6 0 12 0z" fill="#67371f"/><circle cx="12" cy="11.5" r="4.5" fill="#f3f2f0"/></svg>
      <span>218 Lanxi Road, China<br>(Shanghai) Pilot Free Trade Zone)</span>
    </div>
    <div class="socials"><span></span><span></span><span></span><span></span></div>
  </div>
  <div class="footer-rule"></div>
  <div class="copyright">© 2020 Company Name &nbsp;| &nbsp;All Rights Reserved</div>
</footer>

</body>
</html>
```